SkyVelour IOS App for iPhone / Luxury private aviation / 1 main screen

Hello there !

SkyVelour Ltd is a VIP aircraft operator. You can see our https://facebook.example/skyvelour page or our https://instagram.example/sky_velour . Our web page http://skyvelour.example says it all, we don't communicate much except for the music industry activities we have.

We have developed a very simple app, 6 screens total, that will give the user a distance and a flight time between any two airports of the world. Enter a departure point (New York or JFK or KJFK...) and a destination (like Los Angeles, LAX or KLAX) and we will give you the flight time depending on the type of private jet you are selecting in the aircraft database of the app.

You might want to see the attached pdf for the flow...Any design idea is welcome.

We want it to be simple, pure, fast, and of course less will be more. We should see a unity between all these screens, same design spirit of course... On the main screen of the app, we are showing:- the company logo- a departure airport- a destination airport- the selected aircraft with access to a mini photo gallery of the said airplane- a flight time shown in hours and minutes- a distance shown in Miles, Nautical Miles or KM according to the pref page selection- an access to a contact screen- an access to a parameters screen (will develop some of it on a later version).

Thanks !!

Mathis

Target Market(s)

Private aircraft travelers and VIP flights brokers

Industry/Entity Type

Aviation

Font styles to use
Sans Serif

Colors
aaaaaa
5c5c5c
1b1b1b
e9e9e9
ffffff

Requirements
Must have
• Our logo
Nice to have
• Elegant design
Should not have
• Complicated stuff

```html
<!DOCTYPE html>
<html lang="en">
<head>
<meta charset="utf-8">
<title>SkyVelour – App Screens</title>
<link rel="stylesheet" href="https://fonts.googleapis.com/css2?family=Montserrat:wght@400;600;700&family=Raleway:wght@300;400;500&display=swap">
<style>
  :root{
    --sky-top:#bfe3f7;
    --sky-mid:#d7eef6;
    --sky-bottom:#f6efc6;
    --wave-blue:#3aa6ea;
    --wave-deep:#1f8fd8;
    --wave-light:#cfe9f8;
    --accent:#2fa3ee;
    --ink:#1b1b1b;
    --ink-mid:#5c5c5c;
    --ink-soft:#aaaaaa;
    --panel:#e9e9e9;
    --white:#ffffff;
    --label:#b9c6dd;
    --dark-band:#1b1b1b;
  }
  *{box-sizing:border-box;margin:0;padding:0}
  html,body{width:1200px;height:3240px;overflow:hidden;background:var(--white)}
  body{font-family:"Montserrat",Arial,sans-serif;color:var(--ink)}
  .board{position:relative;width:1200px;height:3240px;overflow:hidden;background:var(--white)}

  .backdrop{position:absolute;inset:0;width:1200px;height:3240px}

  .hero-ghost{position:absolute;left:0;top:30px;width:1200px;text-align:center;
    font:700 150px/1 "Montserrat",sans-serif;color:rgba(255,255,255,.28);letter-spacing:4px}
  .hero-title{position:absolute;left:0;top:150px;width:1200px;text-align:center;
    font:600 104px/1 "Montserrat",sans-serif;color:var(--white);letter-spacing:2px}

  /* Splash screen */
  .splash{position:absolute;overflow:hidden;
    background:linear-gradient(180deg,var(--sky-top) 0%,var(--sky-mid) 45%,var(--sky-bottom) 100%)}
  .splash--hero{left:340px;top:355px;width:520px;height:1060px;border-radius:56px;
    box-shadow:0 30px 60px rgba(0,0,0,.18);z-index:3}
  .splash--lower{left:322px;top:1545px;width:300px;height:805px}
  .splash-brand{position:absolute;left:0;width:100%;text-align:center;
    font-family:"Raleway",sans-serif;font-weight:400;color:var(--ink-mid)}
  .splash--hero .splash-brand{top:560px;font-size:38px;letter-spacing:12px}
  .splash--lower .splash-brand{top:420px;font-size:22px;letter-spacing:7px}
  .splash-dot{position:absolute;left:50%;border-radius:50%;background:var(--ink-mid);opacity:.75}
  .splash--hero .splash-dot{top:470px;width:54px;height:54px;margin-left:-27px}
  .splash--lower .splash-dot{top:360px;width:32px;height:32px;margin-left:-16px}

  /* Main flight screen */
  .flight{position:absolute;width:360px;height:780px;background:var(--white);overflow:hidden;
    box-shadow:0 10px 30px rgba(0,0,0,.15);transform-origin:0 0}
  .flight--left{left:14px;top:490px;transform:scale(.9);z-index:2}
  .flight--right{left:862px;top:490px;transform:scale(.9);z-index:2}
  .flight--lower{left:760px;top:1980px}

  .app-bar{height:56px;display:flex;align-items:center;justify-content:space-between;padding:0 16px}
  .menu-icon{width:20px;height:14px;display:flex;flex-direction:column;justify-content:space-between}
  .menu-icon span{display:block;height:2px;background:var(--accent)}
  .app-bar-brand{font:500 11px/1 "Raleway",sans-serif;letter-spacing:3px;color:var(--ink-mid)}

  .route-band{position:relative;height:92px}
  .route-photo{position:absolute;inset:0;background:linear-gradient(100deg,#2b2f2a 0%,#4a4c3c 40%,#1e2320 100%)}
  .route-card{position:absolute;top:18px;width:112px;height:56px;background:var(--white);
    padding:8px 10px}
  .route-card--from{left:14px}
  .route-card--to{right:14px;text-align:right}
  .route-code{font:700 24px/1 "Montserrat",sans-serif;color:var(--ink)}
  .route-city{font:400 7px/1 "Montserrat",sans-serif;color:var(--ink-soft);margin-top:5px;letter-spacing:1px}
  .route-plane{position:absolute;left:50%;top:32px;margin-left:-14px}

  .times{display:grid;grid-template-columns:1fr 1fr 1fr;padding:14px 14px 12px;text-align:center}
  .time-side svg{display:block;margin:0 auto 6px}
  .time-tag{font-size:7px;color:var(--ink-soft)}
  .time-value{font:400 26px/1.1 "Montserrat",sans-serif;color:var(--ink);margin:4px 0}
  .time-place{font-size:6.5px;color:var(--ink-soft)}
  .time-mid{padding-top:4px}
  .mid-label{font-size:6.5px;color:var(--ink-soft);letter-spacing:1px}
  .mid-value{font:600 9px/1.4 "Montserrat",sans-serif;color:var(--accent)}
  .mid-rule{height:1px;background:var(--accent);margin:6px 10px}

  .details{background:var(--panel);margin:0 14px;padding:14px 14px 10px;
    display:grid;grid-template-columns:1fr 1fr;row-gap:14px;column-gap:14px}
  .detail-label{font-size:6.5px;color:var(--ink-soft);letter-spacing:1px}
  .detail-value{font:600 8px/1.4 "Montserrat",sans-serif;color:var(--ink-mid)}
  .detail-links{display:flex;gap:6px;align-items:center}
  .link-dot{width:16px;height:16px;border-radius:50%}
  .link-dot--blue{background:#3b5aa0}
  .link-dot--pink{background:#d6407e}

  .contact-btn{margin:14px 14px 0;height:36px;background:var(--accent);color:var(--white);
    font:700 10px/36px "Montserrat",sans-serif;text-align:center;letter-spacing:1px}

  .distance-bar{position:absolute;left:0;bottom:0;width:100%;height:96px;background:var(--dark-band);
    color:var(--white);padding:12px 14px}
  .distance-title{text-align:center;font:600 7px/1 "Montserrat",sans-serif;letter-spacing:1px;color:#cfcfcf}
  .distance-line{display:flex;align-items:center;gap:8px;margin-top:22px}
  .distance-end{font:600 8px/1.3 "Montserrat",sans-serif;color:var(--white)}
  .distance-end--to{text-align:right}
  .distance-track{flex:1;position:relative;height:2px;background:linear-gradient(90deg,var(--accent),#f4c04a)}
  .distance-track svg{position:absolute;left:50%;top:-8px;margin-left:-9px}

  /* Labels */
  .vertical-name{position:absolute;left:108px;top:1560px;width:60px;
    display:flex;flex-direction:column;align-items:center;gap:32px;
    font:300 58px/1 "Raleway",sans-serif;color:var(--label)}
  .vertical-name span{display:block;transform:rotate(-90deg)}
  .screen-label{position:absolute;font:300 50px/1 "Raleway",sans-serif;color:var(--label);letter-spacing:4px}
  .screen-label--one{left:760px;top:1690px}
  .screen-label--two{left:776px;top:2810px}
</style>
</head>
<body>
<div class="board">

  <svg class="backdrop" viewBox="0 0 1200 3240" aria-hidden="true">
    <defs>
      <linearGradient id="heroSky" x1="0" y1="0" x2="1" y2="1">
        <stop offset="0" stop-color="#7cc4c7"/>
        <stop offset=".5" stop-color="#b6dccb"/>
        <stop offset="1" stop-color="#e2efd8"/>
      </linearGradient>
    </defs>
    <rect x="0" y="0" width="1200" height="1500" fill="url(#heroSky)"/>
    <path d="M0 1150 C 260 1080, 520 1180, 760 1240 C 960 1290, 1100 1230, 1200 1200 L1200 1500 L0 1500 Z" fill="#8fd0f4"/>
    <path d="M0 1000 C 180 1100, 300 1300, 520 1380 C 700 1440, 900 1400, 1200 1380 L1200 1500 L0 1500 Z" fill="var(--wave-blue)"/>
    <path d="M0 1380 C 300 1330, 600 1470, 900 1480 C 1050 1485, 1150 1470, 1200 1460 L1200 1640 C 900 1600, 700 1720, 420 1700 C 220 1690, 80 1620, 0 1600 Z" fill="var(--white)"/>
    <path d="M760 1790 C 900 1760, 1060 1800, 1140 1900 C 1200 1980, 1180 2080, 1120 2120 L 760 2120 Z" fill="var(--wave-light)" opacity=".55"/>
    <path d="M560 1880 C 640 1860, 700 1920, 680 1980 C 660 2040, 600 2060, 560 2030 Z" fill="var(--wave-light)" opacity=".5"/>
    <path d="M640 2420 C 700 2380, 760 2420, 760 2480 L 760 2620 C 700 2640, 640 2600, 640 2540 Z" fill="var(--wave-light)" opacity=".5"/>
  </svg>

  <div class="hero-ghost">SkyVelour</div>
  <h1 class="hero-title">SkyVelour</h1>

  <!-- Flight screen, left -->
  <section class="flight flight--left" aria-label="Flight screen">
    <header class="app-bar">
      <div class="menu-icon"><span></span><span></span><span></span></div>
      <div class="app-bar-brand">SKYVELOUR</div>
      <svg width="14" height="16" viewBox="0 0 14 16"><path d="M7 1c-3 0-4.5 2.2-4.5 5v4L1 12h12l-1.5-2V6C11.5 3.2 10 1 7 1zM5.5 13.5a1.5 1.5 0 0 0 3 0z" fill="var(--accent)"/></svg>
    </header>
    <div class="route-band">
      <div class="route-photo" role="img" aria-label="Photo of a private jet cabin"></div>
      <div class="route-card route-card--from"><div class="route-code">BOS</div><div class="route-city">BOSTON, MA</div></div>
      <svg class="route-plane" width="28" height="28" viewBox="0 0 24 24"><path d="M21 16v-2l-8-5V3.5a1.5 1.5 0 0 0-3 0V9l-8 5v2l8-2.5V19l-2 1.5V22l3.5-1 3.5 1v-1.5L13 19v-5.5z" transform="rotate(90 12 12)" fill="var(--white)"/></svg>
      <div class="route-card route-card--to"><div class="route-code">LHR</div><div class="route-city">LONDON, UK</div></div>
    </div>
    <div class="times">
      <div class="time-side">
        <svg width="18" height="18" viewBox="0 0 24 24"><path d="M21 16v-2l-8-5V3.5a1.5 1.5 0 0 0-3 0V9l-8 5v2l8-2.5V19l-2 1.5V22l3.5-1 3.5 1v-1.5L13 19v-5.5z" transform="rotate(45 12 12)" fill="var(--ink-mid)"/></svg>
        <div class="time-tag">Mid-Size Jet</div><div class="time-value">08:25</div><div class="time-place">Logan International</div>
      </div>
      <div class="time-mid">
        <div class="mid-label">AIRCRAFT</div><div class="mid-value">Velour 45</div>
        <div class="mid-rule"></div>
        <div class="mid-label">FLIGHT TIME</div><div class="mid-value">7H 00M</div>
      </div>
      <div class="time-side">
        <svg width="18" height="18" viewBox="0 0 24 24"><path d="M21 16v-2l-8-5V3.5a1.5 1.5 0 0 0-3 0V9l-8 5v2l8-2.5V19l-2 1.5V22l3.5-1 3.5 1v-1.5L13 19v-5.5z" transform="rotate(135 12 12)" fill="var(--ink-mid)"/></svg>
        <div class="time-tag">Local Arrival</div><div class="time-value">13:25</div><div class="time-place">Heathrow Airport</div>
      </div>
    </div>
    <div class="details">
      <div><div class="detail-label">OPERATOR</div><div class="detail-value">SkyVelour Ltd</div></div>
      <div><div class="detail-label">CREW</div><div class="detail-value">2 Pilots</div></div>
      <div><div class="detail-label">CABIN</div><div class="detail-value">8 Seats</div></div>
      <div><div class="detail-label">CATERING</div><div class="detail-value">Premium</div></div>
      <div><div class="detail-label">BAGGAGE</div><div class="detail-value">50 cu ft</div></div>
      <div class="detail-links"><span class="link-dot link-dot--blue"></span><span class="link-dot link-dot--pink"></span></div>
    </div>
    <div class="contact-btn">CONTACT NOW</div>
    <footer class="distance-bar">
      <div class="distance-title">GREAT CIRCLE DISTANCE: 3,265 NM</div>
      <div class="distance-line">
        <div class="distance-end">BOS<br>08:25</div>
        <div class="distance-track"><svg width="18" height="18" viewBox="0 0 24 24"><path d="M21 16v-2l-8-5V3.5a1.5 1.5 0 0 0-3 0V9l-8 5v2l8-2.5V19l-2 1.5V22l3.5-1 3.5 1v-1.5L13 19v-5.5z" transform="rotate(90 12 12)" fill="var(--white)"/></svg></div>
        <div class="distance-end distance-end--to">LHR<br>13:25</div>
      </div>
    </footer>
  </section>

  <!-- Flight screen, right -->
  <section class="flight flight--right" aria-label="Flight screen">
    <header class="app-bar">
      <div class="menu-icon"><span></span><span></span><span></span></div>
      <div class="app-bar-brand">SKYVELOUR</div>
      <svg width="14" height="16" viewBox="0 0 14 16"><path d="M7 1c-3 0-4.5 2.2-4.5 5v4L1 12h12l-1.5-2V6C11.5 3.2 10 1 7 1zM5.5 13.5a1.5 1.5 0 0 0 3 0z" fill="var(--accent)"/></svg>
    </header>
    <div class="route-band">
      <div class="route-photo" role="img" aria-label="Photo of a private jet cabin"></div>
      <div class="route-card route-card--from"><div class="route-code">BOS</div><div class="route-city">BOSTON, MA</div></div>
      <svg class="route-plane" width="28" height="28" viewBox="0 0 24 24"><path d="M21 16v-2l-8-5V3.5a1.5 1.5 0 0 0-3 0V9l-8 5v2l8-2.5V19l-2 1.5V22l3.5-1 3.5 1v-1.5L13 19v-5.5z" transform="rotate(90 12 12)" fill="var(--white)"/></svg>
      <div class="route-card route-card--to"><div class="route-code">LHR</div><div class="route-city">LONDON, UK</div></div>
    </div>
    <div class="times">
      <div class="time-side">
        <svg width="18" height="18" viewBox="0 0 24 24"><path d="M21 16v-2l-8-5V3.5a1.5 1.5 0 0 0-3 0V9l-8 5v2l8-2.5V19l-2 1.5V22l3.5-1 3.5 1v-1.5L13 19v-5.5z" transform="rotate(45 12 12)" fill="var(--ink-mid)"/></svg>
        <div class="time-tag">Mid-Size Jet</div><div class="time-value">08:25</div><div class="time-place">Logan International</div>
      </div>
      <div class="time-mid">
        <div class="mid-label">AIRCRAFT</div><div class="mid-value">Velour 45</div>
        <div class="mid-rule"></div>
        <div class="mid-label">FLIGHT TIME</div><div class="mid-value">7H 00M</div>
      </div>
      <div class="time-side">
        <svg width="18" height="18" viewBox="0 0 24 24"><path d="M21 16v-2l-8-5V3.5a1.5 1.5 0 0 0-3 0V9l-8 5v2l8-2.5V19l-2 1.5V22l3.5-1 3.5 1v-1.5L13 19v-5.5z" transform="rotate(135 12 12)" fill="var(--ink-mid)"/></svg>
        <div class="time-tag">Local Arrival</div><div class="time-value">13:25</div><div class="time-place">Heathrow Airport</div>
      </div>
    </div>
    <div class="details">
      <div><div class="detail-label">OPERATOR</div><div class="detail-value">SkyVelour Ltd</div></div>
      <div><div class="detail-label">CREW</div><div class="detail-value">2 Pilots</div></div>
      <div><div class="detail-label">CABIN</div><div class="detail-value">8 Seats</div></div>
      <div><div class="detail-label">CATERING</div><div class="detail-value">Premium</div></div>
      <div><div class="detail-label">BAGGAGE</div><div class="detail-value">50 cu ft</div></div>
      <div class="detail-links"><span class="link-dot link-dot--blue"></span><span class="link-dot link-dot--pink"></span></div>
    </div>
    <div class="contact-btn">CONTACT NOW</div>
    <footer class="distance-bar">
      <div class="distance-title">GREAT CIRCLE DISTANCE: 3,265 NM</div>
      <div class="distance-line">
        <div class="distance-end">BOS<br>08:25</div>
        <div class="distance-track"><svg width="18" height="18" viewBox="0 0 24 24"><path d="M21 16v-2l-8-5V3.5a1.5 1.5 0 0 0-3 0V9l-8 5v2l8-2.5V19l-2 1.5V22l3.5-1 3.5 1v-1.5L13 19v-5.5z" transform="rotate(90 12 12)" fill="var(--white)"/></svg></div>
        <div class="distance-end distance-end--to">LHR<br>13:25</div>
      </div>
    </footer>
  </section>

  <!-- Splash screen, hero -->
  <section class="splash splash--hero" aria-label="Splash screen">
    <span class="splash-dot"></span>
    <div class="splash-brand">SKYVELOUR</div>
  </section>

  <!-- Lower presentation -->
  <div class="vertical-name" aria-label="SkyVelour">
    <span>S</span><span>K</span><span>Y</span><span>V</span><span>E</span><span>L</span><span>O</span><span>U</span><span>R</span>
  </div>

  <section class="splash splash--lower" aria-label="Splash screen">
    <span class="splash-dot"></span>
    <div class="splash-brand">SKYVELOUR</div>
  </section>

  <div class="screen-label screen-label--one">SCREEN 1</div>

  <section class="flight flight--lower" aria-label="Flight screen">
    <header class="app-bar">
      <div class="menu-icon"><span></span><span></span><span></span></div>
      <div class="app-bar-brand">SKYVELOUR</div>
      <svg width="14" height="16" viewBox="0 0 14 16"><path d="M7 1c-3 0-4.5 2.2-4.5 5v4L1 12h12l-1.5-2V6C11.5 3.2 10 1 7 1zM5.5 13.5a1.5 1.5 0 0 0 3 0z" fill="var(--accent)"/></svg>
    </header>
    <div class="route-band">
      <div class="route-photo" role="img" aria-label="Photo of a private jet cabin"></div>
      <div class="route-card route-card--from"><div class="route-code">BOS</div><div class="route-city">BOSTON, MA</div></div>
      <svg class="route-plane" width="28" height="28" viewBox="0 0 24 24"><path d="M21 16v-2l-8-5V3.5a1.5 1.5 0 0 0-3 0V9l-8 5v2l8-2.5V19l-2 1.5V22l3.5-1 3.5 1v-1.5L13 19v-5.5z" transform="rotate(90 12 12)" fill="var(--white)"/></svg>
      <div class="route-card route-card--to"><div class="route-code">LHR</div><div class="route-city">LONDON, UK</div></div>
    </div>
    <div class="times">
      <div class="time-side">
        <svg width="18" height="18" viewBox="0 0 24 24"><path d="M21 16v-2l-8-5V3.5a1.5 1.5 0 0 0-3 0V9l-8 5v2l8-2.5V19l-2 1.5V22l3.5-1 3.5 1v-1.5L13 19v-5.5z" transform="rotate(45 12 12)" fill="var(--ink-mid)"/></svg>
        <div class="time-tag">Mid-Size Jet</div><div class="time-value">08:25</div><div class="time-place">Logan International</div>
      </div>
      <div class="time-mid">
        <div class="mid-label">AIRCRAFT</div><div class="mid-value">Velour 45</div>
        <div class="mid-rule"></div>
        <div class="mid-label">FLIGHT TIME</div><div class="mid-value">7H 00M</div>
      </div>
      <div class="time-side">
        <svg width="18" height="18" viewBox="0 0 24 24"><path d="M21 16v-2l-8-5V3.5a1.5 1.5 0 0 0-3 0V9l-8 5v2l8-2.5V19l-2 1.5V22l3.5-1 3.5 1v-1.5L13 19v-5.5z" transform="rotate(135 12 12)" fill="var(--ink-mid)"/></svg>
        <div class="time-tag">Local Arrival</div><div class="time-value">13:25</div><div class="time-place">Heathrow Airport</div>
      </div>
    </div>
    <div class="details">
      <div><div class="detail-label">OPERATOR</div><div class="detail-value">SkyVelour Ltd</div></div>
      <div><div class="detail-label">CREW</div><div class="detail-value">2 Pilots</div></div>
      <div><div class="detail-label">CABIN</div><div class="detail-value">8 Seats</div></div>
      <div><div class="detail-label">CATERING</div><div class="detail-value">Premium</div></div>
      <div><div class="detail-label">BAGGAGE</div><div class="detail-value">50 cu ft</div></div>
      <div class="detail-links"><span class="link-dot link-dot--blue"></span><span class="link-dot link-dot--pink"></span></div>
    </div>
    <div class="contact-btn">CONTACT NOW</div>
    <footer class="distance-bar">
      <div class="distance-title">GREAT CIRCLE DISTANCE: 3,265 NM</div>
      <div class="distance-line">
        <div class="distance-end">BOS<br>08:25</div>
        <div class="distance-track"><svg width="18" height="18" viewBox="0 0 24 24"><path d="M21 16v-2l-8-5V3.5a1.5 1.5 0 0 0-3 0V9l-8 5v2l8-2.5V19l-2 1.5V22l3.5-1 3.5 1v-1.5L13 19v-5.5z" transform="rotate(90 12 12)" fill="var(--white)"/></svg></div>
        <div class="distance-end distance-end--to">LHR<br>13:25</div>
      </div>
    </footer>
  </section>

  <div class="screen-label screen-label--two">SCREEN 2</div>

</div>
</body>
</html>
```